CareWillow Brand Standards and Core Values

I would like to have frameable posters made up for each office using our brand standards. I would like the posters to include:Our Vision Statement:We are transforming the healthcare staffing and homecare industry with our people-oriented, world-class team. Clients choose us, and develop lasting bonds with our team because of our impeccably high standards and our reputation for always remembering this is, first and foremost, a people business. We consistently go the extra mile to ensure our nurses and those being cared for are at all times, treated with dignity and respect. We hold ourselves and those we work with to the highest possible standards. We consistently deliver what we promise, and whenever possible, even more. Our Mission Statement:We go above and beyond to ensure our clients receive the right care and the right people at the right time. Our rigorous recruitment standards result in strong caregivers who are trusted for their expertise, experience and compassion. Our Values:Through our genuine caring and compassion, we are committed to honor all with whom we interact. We are grounded in our faith and dedicated to working together as a family that consistently and passionately lives our values. Compassion Integrity and honesty Faith Decisive action Constant and never-ending improvement Personal ownership Excellence Positive attitude Passion RespectWho we are:We are friendly, servant leaders who have a sense of urgency to meet the needs of our nurses and clients. We prioritize personal relationships with genuine caring and compassion. We inspire others through our passion and energy.Our main colors are: HEX# 5C80DE, HEX# BDE080, HEX# 8C8C8Caccent colors are: HEX# 95D6E3, HEX# AD59AB, HEX# 002E57

Target Market(s)

office employee inspiration

Font styles to use
Other font styles liked:
• Verdana

Colors

Designer to choose colors to be used in the design.

Requirements
Must have
• the core values listed in description
Nice to have
• colors given in description, something fun and inspiring for office employees to help motivate them !
Should not have
• colors that are not company colors. I have listed HEX codes in description

```html
<!DOCTYPE html>
<html lang="en">
<head>
<meta charset="utf-8">
<title>CareWillow – Our Values Poster</title>
<link rel="stylesheet" href="https://fonts.googleapis.com/css2?family=Noto+Sans:wght@400;700;800&display=swap">
<style>
  :root {
    --brand-blue: #5C80DE;
    --brand-green: #BDE080;
    --brand-grey: #8C8C8C;
    --accent-aqua: #95D6E3;
    --accent-purple: #AD59AB;
    --accent-navy: #002E57;
    --white: #FFFFFF;
    --backdrop: #EDEDED;
  }
  * { margin: 0; padding: 0; box-sizing: border-box; }
  html, body {
    width: 1200px;
    height: 1138px;
    overflow: hidden;
    background: var(--backdrop);
  }
  .poster {
    position: absolute;
    left: 198px;
    top: 19px;
    width: 804px;
    height: 1100px;
    background: var(--brand-green);
    font-family: Verdana, "Noto Sans", sans-serif;
  }
  .poster__title {
    position: absolute;
    top: 42px;
    left: 0;
    width: 100%;
    text-align: center;
    color: var(--white);
    font-family: Verdana, "Noto Sans", sans-serif;
    font-weight: 800;
    font-size: 70px;
    letter-spacing: 2px;
    line-height: 1;
  }
  .poster__artwork {
    position: absolute;
    left: 59px;
    top: 128px;
    width: 665px;
    height: 496px;
    display: block;
  }
  .values-headline {
    position: absolute;
    left: 0;
    top: 0;
    width: 100%;
    height: 100%;
    pointer-events: none;
  }
  .values-headline__line {
    position: absolute;
    white-space: nowrap;
    line-height: 1;
    font-family: Verdana, "Noto Sans", sans-serif;
    font-weight: 400;
  }
  .values-headline__line--compassion {
    left: 188px;
    top: 656px;
    font-size: 50px;
    letter-spacing: 4px;
    color: var(--brand-blue);
  }
  .values-headline__line--integrity {
    left: 188px;
    top: 714px;
    font-size: 48px;
    color: var(--white);
  }
  .values-headline__line--honesty {
    left: 342px;
    top: 768px;
    font-size: 48px;
    color: var(--white);
  }
  .poster__body {
    position: absolute;
    left: 30px;
    top: 836px;
    width: 747px;
    color: var(--accent-navy);
    font-size: 14.4px;
    line-height: 21.6px;
    text-align: justify;
  }
  .brand-mark {
    position: absolute;
    right: 48px;
    bottom: 38px;
    display: flex;
    align-items: center;
    gap: 12px;
  }
  .brand-mark__dot {
    width: 22px;
    height: 22px;
    border-radius: 50%;
    background: var(--white);
  }
  .brand-mark__name {
    color: var(--white);
    font-family: Verdana, "Noto Sans", sans-serif;
    font-weight: 400;
    font-size: 28px;
    line-height: 1;
  }
</style>
</head>
<body>
  <main class="poster">
    <h1 class="poster__title">OUR VALUES</h1>

    <svg class="poster__artwork" viewBox="0 0 665 496" role="img" aria-label="Illustration of a purple lotus flower rising from two open blue hands, surrounded by aqua butterflies">
      <defs>
        <linearGradient id="artwork-fill" x1="0" y1="0" x2="0" y2="1">
          <stop offset="0" stop-color="#AD59AB" stop-opacity="0.55"/>
          <stop offset="1" stop-color="#5C80DE" stop-opacity="0.55"/>
        </linearGradient>
      </defs>
      <rect width="665" height="496" fill="url(#artwork-fill)"/>
    </svg>

    <div class="values-headline">
      <p class="values-headline__line values-headline__line--compassion">COMPASSION</p>
      <p class="values-headline__line values-headline__line--integrity">INTEGRITY &amp;</p>
      <p class="values-headline__line values-headline__line--honesty">HONESTY</p>
    </div>

    <p class="poster__body">Through our genuine caring and compassion, we are committed to honor all with whom we interact. We are grounded in our faith and dedicated to working together as a family that consistently and passionately lives our values. Compassion Integrity and honesty Faith Decisive action Constant and never-ending improvement Personal ownership Excellence Positive attitude Passion RespectWho we are:We are friendly, servant leaders who have a sense of urgency to meet the needs of our nurses and clients. We prioritize personal relationships with genuine caring and compassion. We inspire others through our passion and energy.</p>

    <div class="brand-mark">
      <span class="brand-mark__dot"></span>
      <span class="brand-mark__name">CareWillow</span>
    </div>
  </main>
</body>
</html>
```